Business Card and Stationery for Interior Design Company
Silver Kettle Design
Designers,
On the back of my card on want the following services listed:
Interior Decorating
Room Redesign
Space Planning
Paint Color Selection
Furnishings & Accessories
The fonts used in the logo are as follows:
fonts:
Kozuka Mincho Pr6N M
Miss Le Gatees (modified)
RT/KPF/JN Team
My tagline "Rooms with Intent" does NOT have to be the same font as the original logo font. Neither does my Name. In fact, tagline should probably be italic and my Name I'd like to see perhaps in a similar script font like the word INTERIOR.

```html
<!DOCTYPE html>
<html lang="en">
<head>
<meta charset="utf-8">
<title>Silver Kettle Design — Business Card</title>
<link rel="stylesheet" href="https://fonts.googleapis.com/css2?family=Shippori+Mincho:wght@500&family=Great+Vibes&family=Cormorant+Garamond:ital,wght@1,500&display=swap">
<style>
  :root {
    --backdrop: #1c1c1e;
    --card: #ffffff;
    --stripe: #f0f0f0;
    --frame: #d2d2d2;
    --ink: #5a5a5a;
    --gold: #c9a34a;
    --teal: #93d6d2;
    --tagline-ink: #3f4a4a;
  }
  * { box-sizing: border-box; margin: 0; padding: 0; }
  html, body {
    width: 1200px; height: 901px; overflow: hidden;
    background: var(--backdrop);
  }
  .canvas {
    width: 1200px; height: 901px;
    display: flex; justify-content: center; align-items: center; gap: 80px;
  }
  .card {
    position: relative;
    width: 400px; height: 700px;
    background: repeating-linear-gradient(90deg, var(--card) 0 40px, var(--stripe) 40px 80px);
    border-radius: 6px;
    box-shadow: 0 10px 30px rgba(0,0,0,.5);
    overflow: hidden;
  }
  .card__frame {
    position: absolute; inset: 18px;
    border: 1.5px solid var(--frame);
    border-radius: 8px;
  }
  .card__band {
    position: absolute; left: 18px; right: 18px; bottom: 18px; height: 120px;
    background: var(--teal);
    border-radius: 0 0 8px 8px;
    display: flex; align-items: center; justify-content: center;
  }
  .tagline {
    font-family: "Cormorant Garamond", serif;
    font-style: italic; font-weight: 500;
    font-size: 38px; letter-spacing: .5px; color: var(--tagline-ink);
  }
  .logo {
    position: absolute; left: 0; right: 0; top: 70px;
    display: flex; flex-direction: column; align-items: center; gap: 18px;
  }
  .logo__mark { width: 90px; height: 90px; background: var(--teal); }
  .logo__name {
    font-family: "Shippori Mincho", serif; font-weight: 500;
    font-size: 36px; line-height: 1.1; color: var(--ink);
    text-align: center;
  }
  .contact {
    position: absolute; left: 60px; right: 40px; top: 360px;
  }
  .contact__person {
    font-family: "Great Vibes", cursive;
    font-size: 40px; line-height: 1.2; color: var(--gold);
  }
  .contact__rule {
    width: 260px; height: 1.5px; background: var(--gold); margin: 6px 0 16px;
  }
  .contact__line {
    font-family: "Shippori Mincho", serif; font-weight: 500;
    font-size: 17px; line-height: 1.55; color: var(--ink);
  }
  .card--back .logo { top: 60px; gap: 14px; }
  .card--back .logo__mark { width: 70px; height: 70px; }
  .card--back .logo__name { font-size: 30px; }
  .services {
    position: absolute; left: 50px; right: 50px; top: 290px;
    border: 1.5px solid var(--gold);
    padding: 22px 20px;
    list-style: none; text-align: center;
    background: rgba(255,255,255,.7);
  }
  .services li {
    font-family: "Shippori Mincho", serif; font-weight: 500;
    font-size: 18px; line-height: 1.9; color: var(--ink);
  }
</style>
</head>
<body>
<main class="canvas">
  <article class="card card--front">
    <div class="card__frame"></div>
    <header class="logo">
      <div class="logo__mark"></div>
      <div class="logo__name">Silver Kettle<br>Design</div>
    </header>
    <section class="contact">
      <p class="contact__person">Tessa Robanik</p>
      <div class="contact__rule"></div>
      <p class="contact__line">555-014-2290</p>
      <p class="contact__line">tessa@silverkettledesign.com</p>
      <p class="contact__line">www.silverkettledesign.com</p>
    </section>
    <footer class="card__band"><span class="tagline">Rooms with Intent</span></footer>
  </article>

  <article class="card card--back">
    <div class="card__frame"></div>
    <header class="logo">
      <div class="logo__mark"></div>
      <div class="logo__name">Silver Kettle<br>Design</div>
    </header>
    <ul class="services">
      <li>Interior Decorating</li>
      <li>Room Redesign</li>
      <li>Space Planning</li>
      <li>Paint Color Selection</li>
      <li>Furnishings &amp; Accessories</li>
    </ul>
    <footer class="card__band"><span class="tagline">Rooms with Intent</span></footer>
  </article>
</main>
</body>
</html>
```